Glow in the Dark Inks Sales Flyer - Targeted to the music industry

We need help!
We need a creative flyer to tell the music industry about our new, colorful glow in the dark inks that look amazing on T-shirts and concert merchandise.

The flyer will go to merchandising managers for bands around the world. The design needs to be hip and contemporary but not offensive. No f-bombs please! Size is 4” x 6” or 3” x 5”, and will be printed on card stock. Design can be both sides if you want. We expect color but black and white with some fluorescent accents could be cool. Surprise us.
Here’s some copy, and we can fill in the contact info when the design is close to final.

Help your fans get lit with branded T-shirts and merchandise that glows in the dark!

Let our new Starwell Inks light up your next show!

Call us now –
Updates

Hello Designers.

Please keep in mind that although the thought of glow-in-the-dark may trigger a glowing, green color in your creative minds, StarWell Inks has a wide variety of colors to bring to offer. So please be sure to show that it's not only green glow we are promoting but we have a wide range of colors that glow (including pink, purple, white that glow blue, blue, green, orange, yellow, etc.)

Thank you!

```html
<!DOCTYPE html>
<html lang="en">
<head>
<meta charset="utf-8">
<title>Starwell Inks – Glow in the Dark Inks Flyer</title>
<link rel="stylesheet" href="https://fonts.googleapis.com/css2?family=Comfortaa:wght@500;600;700&display=swap">
<style>
  :root {
    --page: #ffffff;
    --glow-white: #ffffff;
    --glow-mint: #b8f5c8;
    --glow-green: #c6ffb0;
    --glow-pink: #ffb8f5;
    --glow-orange: #ffcf7a;
    --glow-blue: #9ae8ff;
    --glow-lilac: #e0a8ff;
    --answer: #5a1e8a;
    --note-pink: #ff3cf0;
    --ink-dark: #2a0a4a;
  }
  * { margin: 0; padding: 0; box-sizing: border-box; }
  html, body { width: 1200px; height: 900px; overflow: hidden; background: var(--page); }
  body { position: relative; font-family: "Comfortaa", "Arial Rounded MT Bold", sans-serif; font-weight: 600; }

  .flyer-side { position: absolute; top: 12px; width: 576px; height: 873px; overflow: hidden; }
  .flyer-side--front { left: 12px; }
  .flyer-side--back { left: 612px; }

  .backdrop { position: absolute; inset: 0; }
  .flyer-side--front .backdrop {
    background:
      radial-gradient(ellipse at 80% 70%, rgba(240,80,240,.85), transparent 60%),
      radial-gradient(ellipse at 20% 20%, rgba(120,50,200,.7), transparent 60%),
      linear-gradient(160deg, #4a1a9a 0%, #8a2ad0 45%, #c43ae0 75%, #8a22c8 100%);
  }
  .flyer-side--back .backdrop {
    background:
      radial-gradient(ellipse at 70% 25%, rgba(200,70,230,.8), transparent 55%),
      radial-gradient(ellipse at 25% 80%, rgba(90,30,170,.8), transparent 60%),
      linear-gradient(200deg, #7a28c8 0%, #5a1ea8 50%, #3e1680 100%);
  }

  .line { position: absolute; white-space: nowrap; line-height: 1; }

  .glow-white  { color: var(--glow-white);  text-shadow: 0 0 4px #fff, 0 0 10px #f6c8ff, 0 0 20px #e090ff; }
  .glow-mint   { color: var(--glow-mint);   text-shadow: 0 0 4px #d8ffe0, 0 0 12px #7ef0a0, 0 0 22px #40c080; }
  .glow-green  { color: var(--glow-green);  text-shadow: 0 0 6px #e0ffd0, 0 0 16px #80ff70, 0 0 30px #40e060; }
  .glow-pink   { color: var(--glow-pink);   text-shadow: 0 0 4px #ffe0fa, 0 0 12px #ff70f0, 0 0 22px #e030e0; }
  .glow-orange { color: var(--glow-orange); text-shadow: 0 0 4px #fff0c0, 0 0 12px #ffa030, 0 0 22px #ff8000; }
  .glow-blue   { color: var(--glow-blue);   text-shadow: 0 0 4px #e0f8ff, 0 0 12px #40c8ff, 0 0 22px #2090ff; }
  .glow-lilac  { color: var(--glow-lilac);  text-shadow: 0 0 4px #f4e0ff, 0 0 14px #b060ff, 0 0 26px #8040e0; }

  .q { font-size: 40px; font-weight: 700; letter-spacing: 1px; }
  .mean-more { font-size: 38px; font-weight: 700; }
  .mean-more .emph { font-size: 50px; }
  .answer-lead {
    font-size: 36px; font-weight: 500; letter-spacing: 1px; color: var(--answer);
    text-shadow: 0 0 3px #fff, 0 0 10px #f0b0ff, 0 0 18px #e080ff;
  }
  .answer { font-size: 92px; font-weight: 500; letter-spacing: 4px; }

  .tagline {
    position: absolute; left: 0; right: 0; text-align: center;
    font-size: 18px; font-weight: 700; line-height: 28px;
  }
  .tagline--front {
    top: 726px; color: var(--note-pink);
    text-shadow: 1px 1px 0 #fff, -1px -1px 0 #fff, 1px -1px 0 #fff, -1px 1px 0 #fff;
  }
  .tagline--back {
    top: 740px; color: #fff;
    text-shadow: 1px 1px 0 var(--ink-dark), -1px -1px 0 var(--ink-dark), 1px -1px 0 var(--ink-dark), -1px 1px 0 var(--ink-dark);
  }

  .pitch {
    position: absolute; left: 0; right: 0; text-align: center;
    font-size: 13px; font-weight: 700; line-height: 19px; color: #fff;
  }
  .pitch--front { top: 808px; }
  .pitch--back { top: 814px; }
  .brand-name { color: var(--glow-green); }

  .s { font-size: 56px; font-weight: 700; }
  .s-big { font-size: 60px; }
  .glow-word { font-size: 96px; font-weight: 500; }
  .glow-word--mid { font-size: 112px; }
  .glow-word--large { font-size: 132px; }
</style>
</head>
<body>

<section class="flyer-side flyer-side--front">
  <div class="backdrop" role="img" aria-label="Purple and magenta grunge texture with splatters, circles and technical line ornaments"></div>

  <p class="line q glow-white" style="left:18px; top:28px;">Have You</p>
  <p class="line q glow-white" style="left:143px; top:68px;">ever wondered</p>
  <p class="line q glow-white" style="left:18px; top:108px;">about the words</p>
  <p class="line q glow-white" style="left:343px; top:153px;">you say?</p>

  <p class="line q glow-white" style="left:108px; top:233px;">Have You</p>
  <p class="line q glow-white" style="left:36px; top:273px;">ever asked yourself,</p>
  <p class="line q glow-white" style="left:128px; top:313px;">can I make</p>
  <p class="line q glow-white" style="left:306px; top:358px;">my words</p>

  <p class="line mean-more glow-white" style="left:128px; top:436px;">mean <span class="emph">more?</span></p>

  <p class="line answer-lead" style="left:110px; top:550px;">The answer is...</p>
  <p class="line answer glow-green" style="left:18px; top:614px;">You Can</p>

  <p class="tagline tagline--front">All you need is glow in the dark ink<br>on a T-shirt or wherever you want</p>
  <p class="pitch pitch--front">Help your fans get lit with branded T-shirts<br>and merchandise that glows in the dark!</p>
</section>

<section class="flyer-side flyer-side--back">
  <div class="backdrop" role="img" aria-label="Deep purple grunge texture with pink bubbles, diagonal streaks and line ornaments"></div>

  <p class="line s glow-mint" style="left:53px; top:66px;">How much</p>
  <p class="line s glow-mint" style="left:203px; top:136px;">You said</p>
  <p class="line s glow-mint" style="left:53px; top:206px;">is <span class="s-big glow-pink">expressed</span></p>
  <p class="line s glow-mint" style="left:196px; top:282px;">by</p>
  <p class="line s glow-mint" style="left:88px; top:360px;">the way</p>
  <p class="line s glow-mint" style="left:143px; top:432px;">your words</p>

  <p class="line glow-word glow-orange" style="left:160px; top:508px;">glow</p>
  <p class="line glow-word glow-word--mid glow-blue" style="left:122px; top:550px;">glow</p>
  <p class="line glow-word glow-word--large glow-lilac" style="left:90px; top:588px;">glow</p>

  <p class="tagline tagline--back">All you need is glow in the dark ink<br>on a T-shirt or wherever you want</p>
  <p class="pitch pitch--back">Let our new <span class="brand-name">Starwell Inks</span> light up your next show!<br>Pink, purple, blue, green, orange, yellow and more. Call us now.</p>
</section>

</body>
</html>
```